Flyer für Lach- und Humorworkshops
Zielgruppe
Ich biete Lach- und Humorworkshops an für Unternehmen und Privatpersonen, für mehr Lebensfreude und Erfolg, ob privat oder im Business.
Aufgabenstellung
- DIN A6
- Textvorgabe im Word kann auch gekürzt werden, je nach Platz auf dem Flyer
- Schlagwörter wie 'Lachen' in der Schrift 'Licorice' so wie auf der Website

```html
<!DOCTYPE html>
<html lang="de">
<head>
<meta charset="utf-8">
<title>Lach-Workshop Flyer</title>
<link href="https://fonts.googleapis.com/css2?family=Licorice&family=Raleway:wght@400;500;700;800&display=swap" rel="stylesheet">
<style>
  :root {
    --rose: #a56a63;
    --rose-mid: #c39089;
    --blush: #efd6d2;
    --teal: #5cbcc6;
    --gold: #c4a04c;
    --ink: #2b2322;
    --paper: #ffffff;
    --stage: #e6e1e0;
    --illu-a: #f1ede6;
    --illu-b: #3f7f86;
    --photo-a: #dfe2e3;
    --photo-b: #b9bdbf;
  }
  * { box-sizing: border-box; margin: 0; padding: 0; }
  html, body { width: 1200px; height: 1200px; overflow: hidden; }
  body {
    background: var(--stage);
    font-family: "Raleway", sans-serif;
    color: var(--ink);
    position: relative;
  }
  .flyer {
    position: absolute;
    top: 204px;
    width: 560px;
    height: 792px;
    background: var(--paper);
    overflow: hidden;
    box-shadow: 0 2px 10px rgba(0,0,0,.08);
  }
  .flyer--front { left: 25px; }
  .flyer--back { left: 615px; }
  .abs { position: absolute; }

  /* Front */
  .front-accent-square { left: 320px; top: 0; width: 160px; height: 90px; background: var(--blush); }
  .front-illustration {
    left: 240px; top: 70px; width: 320px; height: 350px;
    background: linear-gradient(135deg, var(--illu-b) 0%, #8fb3b0 22%, var(--illu-a) 48%, var(--illu-a) 100%);
  }
  .brand-name { left: 28px; top: 150px; font-weight: 500; font-size: 30px; color: var(--gold); letter-spacing: .5px; }
  .bracket-top { left: 170px; top: 190px; width: 80px; height: 12px; background: var(--rose-mid); }
  .bracket-side { left: 170px; top: 190px; width: 12px; height: 250px; background: var(--rose-mid); }
  .front-blush-box { left: 300px; top: 410px; width: 170px; height: 50px; background: var(--blush); }
  .front-rose-bar { left: 470px; top: 420px; width: 90px; height: 25px; background: var(--rose); }
  .script-headline {
    left: 62px; top: 188px;
    z-index: 2;
    font-family: "Licorice", cursive;
    font-weight: 400;
    font-size: 80px; line-height: 64px;
    color: var(--teal);
  }
  .script-headline span { display: block; }
  .script-headline span:nth-child(2) { padding-left: 55px; }
  .script-headline span:nth-child(3) { padding-left: 70px; }
  .question-band {
    left: 0; top: 440px; width: 430px; height: 92px;
    background: var(--blush); padding: 8px 0 0 28px;
    color: var(--rose); text-transform: uppercase;
  }
  .question-band .q-small { font-size: 17px; font-weight: 400; line-height: 20px; }
  .question-band .q-mid { font-size: 27px; font-weight: 800; line-height: 28px; }
  .question-band .q-big { font-size: 38px; font-weight: 800; line-height: 38px; }
  .front-intro { left: 28px; top: 544px; width: 510px; font-size: 14px; line-height: 19px; font-weight: 500; }
  .portrait-frame { left: 0; top: 604px; width: 272px; height: 188px; background: var(--rose); }
  .portrait-photo {
    left: 14px; top: 618px; width: 244px; height: 174px;
    background: linear-gradient(180deg, var(--photo-a), var(--photo-b));
  }
  .why-block { left: 290px; top: 600px; width: 250px; }
  .why-block h2 { font-size: 24px; font-weight: 800; color: var(--rose); margin-bottom: 5px; }
  .why-block ul { list-style: none; font-size: 13px; line-height: 17px; font-weight: 500; }
  .why-block li { padding-left: 12px; position: relative; margin-bottom: 2px; }
  .why-block li::before { content: "•"; position: absolute; left: 0; }

  /* Back */
  .workshop-intro { left: 28px; top: 24px; width: 505px; font-size: 12.5px; line-height: 17px; font-weight: 500; }
  .workshop-intro h2 { font-size: 22px; font-weight: 800; color: var(--rose); text-transform: uppercase; margin-bottom: 4px; }
  .workshop-intro p + p { margin-top: 6px; }
  .business-band { left: 0; top: 168px; width: 560px; height: 92px; background: var(--rose); }
  .business-title { left: 28px; top: 178px; color: var(--paper); text-transform: uppercase; }
  .business-title .b-light { font-size: 19px; font-weight: 400; line-height: 22px; }
  .business-title .b-bold { font-size: 24px; font-weight: 800; line-height: 27px; }
  .business-text { left: 28px; top: 272px; width: 505px; font-size: 12.5px; line-height: 17px; font-weight: 500; }
  .humor-lead { left: 28px; top: 382px; width: 505px; font-size: 12.5px; line-height: 17px; font-weight: 500; }
  .humor-lead strong { font-size: 19px; font-weight: 800; color: var(--rose); }
  .back-blush-box { left: 28px; top: 440px; width: 170px; height: 120px; background: var(--blush); }
  .topic-list { left: 220px; top: 430px; list-style: none; font-size: 12.5px; line-height: 19px; font-weight: 500; }
  .topic-list li::before { content: "• "; }
  .about-panel { left: 0; top: 548px; width: 560px; height: 244px; background: var(--rose-mid); }
  .about-photo-frame { left: 28px; top: 530px; width: 300px; height: 236px; background: var(--paper); }
  .about-photo {
    left: 36px; top: 538px; width: 284px; height: 220px;
    background: linear-gradient(180deg, var(--photo-a), var(--photo-b));
  }
  .about-text { left: 348px; top: 572px; width: 190px; color: var(--paper); font-size: 13px; line-height: 18px; font-weight: 500; }
  .about-text h2 { font-size: 24px; font-weight: 800; margin-bottom: 6px; }
</style>
</head>
<body>

<section class="flyer flyer--front">
  <div class="abs front-accent-square"></div>
  <div class="abs front-illustration" role="img" aria-label="Aquarell-Illustration einer lachenden Frau mit Blumen im Haar"></div>
  <div class="abs brand-name">heiterra</div>
  <div class="abs bracket-top"></div>
  <div class="abs bracket-side"></div>
  <div class="abs front-blush-box"></div>
  <div class="abs front-rose-bar"></div>
  <div class="abs question-band">
    <div class="q-small">Wann hast du das letzte</div>
    <div class="q-mid">Mal so richtig</div>
    <div class="q-big">Gelacht?</div>
  </div>
  <h1 class="abs script-headline"><span>Lachen</span><span>ist wie</span><span>kurzferien</span></h1>
  <p class="abs front-intro">Lachen ist nicht nur ein Ausdruck von Freude, es ist gesund für unseren Körper, ausgleichend für unseren Geist und Balsam für unsere Seele.</p>
  <div class="abs portrait-frame"></div>
  <div class="abs portrait-photo" role="img" aria-label="Foto der lachenden Lach-Trainerin"></div>
  <div class="abs why-block">
    <h2>WARUM LACHEN?</h2>
    <ul>
      <li>Lachen ist einfach, gesund und macht glücklich.</li>
      <li>Lachen ist eine universelle Sprache, die verbindet.</li>
      <li>Lachen ist sofort wirksam und nachhaltig zugleich.</li>
      <li>Lachen ist ganzheitlich, nachhaltig und sinnvoll.</li>
    </ul>
  </div>
</section>

<section class="flyer flyer--back">
  <div class="abs workshop-intro">
    <h2>Lach-Workshop</h2>
    <p>Du suchst eine besondere Teambuilding Aktivität? Wie wäre es mit einer kurzen Auszeit aus dem Alltag, die lustig, gesund, nachhaltig und sinnvoll ist?</p>
    <p>In einem Lach-Workshop geht es in erster Linie darum, gemeinsam Spass zu haben und ausgiebig zu lachen.</p>
  </div>
  <div class="abs business-band"></div>
  <div class="abs business-title">
    <div class="b-light">Humor im Business</div>
    <div class="b-bold">Für ein positives</div>
    <div class="b-bold">Betriebsklima</div>
  </div>
  <p class="abs business-text">Lachen ist gesund – das gilt nicht nur für unsere persönliche Gesundheit, sondern auch für ein Unternehmen. Lachen ist eine universelle, positive Form der Kommunikation. Lachen ist essentiell für zwischenmenschliche Beziehungen, denn Lachen schafft Vertrauen und Nähe. Wo gelacht wird, fühlen wir uns wohl, der Teamgeist wird gestärkt, Kreativität und Leistungsbereitschaft werden gefördert.</p>
  <p class="abs humor-lead"><strong>Lachen &amp; Humor</strong> lässt sich sehr vielseitig integrieren, kann einen Anlass bereichern oder ergänzen:</p>
  <div class="abs back-blush-box"></div>
  <ul class="abs topic-list">
    <li>Teambuilding</li>
    <li>Persönlichkeitsentwicklung</li>
    <li>Stressmanagement</li>
    <li>Gesundheit &amp; Wohlbefinden</li>
    <li>Kreaktivität &amp; Innovation</li>
  </ul>
  <div class="abs about-panel"></div>
  <div class="abs about-photo-frame"></div>
  <div class="abs about-photo" role="img" aria-label="Foto der Lach-Trainerin, lachend auf dem Boden liegend"></div>
  <div class="abs about-text">
    <h2>ÜBER MICH:</h2>
    <p>Ich lache fürs Leben gerne! Als Lach-Trainerin habe ich es mir zur Aufgabe gemacht, Menschen mit Lachen &amp; Humor zu inspirieren.</p>
  </div>
</section>

</body>
</html>
```